Consulting Practice for Charities Needs A Brochure Deisgn

Hi! We need a tri-fold brochure for a Washington, DC based consulting practice that works with charities (NGOs, Associations, etc.) and wealthy donors (philanthropists). Our company, Morrow Civic Advisors, helps nonprofits to implement practices that maximize organizational efficiency and effectiveness - by working directly with board members and staff.
Our clients are well educated and quite sophisticated (some charities are international with multi-million dollar budgets, while others are quite local and small) This brochure will be handed to them by some of our 'referral partners' (law firms, accountants and even governmental agencies) in addition to being given out during our presentations. We draw inspiration from nature and would like to somehow include a "natural / eco-friendly" feel to the piece, including natural colors .... that being said, not in any way "folksy" - it must be sophisticated.

Target Market(s)

nonprofit executive directors, board chairs, wealth holders (philanthropists)

Industry/Entity Type

Consulting

Requirements
Must have
• I uploaded a word file with content (text) - most of that needs to be on the brochure ... but ... if it looks too crowded, let me know and I'll reduce
Nice to have
• pop-out quotes (maybe from testimonials??), nature - theme of some kind but also photo of boardroom (links to samples are like are uploaded in a word doc below)
Should not have
• nothing cute ... nothing too feminine

```html
<!DOCTYPE html>
<html lang="en">
<head>
<meta charset="utf-8">
<title>Morrow Civic Advisors – Tri-fold Brochure</title>
<link href="https://fonts.googleapis.com/css2?family=Arvo:wght@400;700&family=Lora:wght@400;500&display=swap" rel="stylesheet">
<style>
  :root {
    --stage: #d4d5d7;
    --paper: #ffffff;
    --purple: #7d74b5;
    --orange: #f39323;
    --quote-grey: #8f9093;
    --text: #4d4d4f;
  }
  * { box-sizing: border-box; margin: 0; padding: 0; }
  html, body { width: 1200px; height: 970px; overflow: hidden; }
  body { background: var(--stage); font-family: "Lora", Georgia, serif; color: var(--text); position: relative; }

  .brochure { position: absolute; left: 64px; top: 72px; width: 1072px; height: 833px; background: var(--paper); overflow: hidden; }
  .panel { position: absolute; top: 0; height: 100%; width: 358px; }
  .panel--left { left: 0; }
  .panel--middle { left: 358px; background: linear-gradient(to right, #f1f1f2, #fbfbfb 10%, #fff 50%); }
  .panel--right { left: 716px; background: linear-gradient(to right, #ededee, #fbfbfb 8%, #fff 40%); }

  .scene { position: absolute; }
  .scene--lake-top { left: 0; top: 0; width: 716px; height: 260px; }
  .scene--left-shore { left: 0; top: 640px; width: 358px; height: 150px; background: linear-gradient(to bottom, rgba(255,255,255,0), #6c7d65 25%, #3f5539 60%, #55625f 100%); }
  .scene--middle-lake { left: 358px; top: 300px; width: 358px; height: 490px; background: linear-gradient(to bottom, #ffffff 0%, #e9ecee 25%, #cfd6dc 40%, #3d5738 55%, #536867 70%, #6b7561 85%, #4d5a3d 100%); }
  .scene--right-forest { left: 716px; top: 520px; width: 356px; height: 270px; background: linear-gradient(to bottom, rgba(255,255,255,0), #8aa07e 20%, #3a5533 45%, #5d6f73 75%, #45533e 100%); }

  .headline { position: absolute; left: 390px; top: 62px; width: 270px; text-align: center; color: #fff; font-family: "Arvo", Georgia, serif; font-weight: 400; font-size: 24px; line-height: 31px; text-shadow: 0 0 4px rgba(0,0,0,.85), 1px 1px 3px rgba(0,0,0,.7); }
  .headline strong { font-weight: 700; display: block; }

  .what-we-do { position: absolute; left: 36px; top: 250px; width: 290px; }
  .section-title { font-family: "Arvo", Georgia, serif; font-weight: 700; color: var(--purple); font-size: 21px; margin-bottom: 10px; }
  .subhead { color: var(--orange); font-size: 14px; font-weight: 500; line-height: 16px; }
  .body-copy { font-size: 13px; line-height: 15.9px; }
  .body-copy + .subhead { margin-top: 14px; }

  .brand { position: absolute; left: 716px; top: 0; width: 356px; height: 140px; display: flex; align-items: center; justify-content: center; gap: 10px; }
  .brand__mark { width: 22px; height: 22px; border-radius: 50%; background: var(--purple); }
  .brand__name { font-family: "Arvo", Georgia, serif; font-size: 22px; color: var(--purple); font-weight: 400; }

  .services { position: absolute; left: 745px; top: 155px; width: 320px; }
  .services__title { font-family: "Arvo", Georgia, serif; color: var(--orange); font-size: 25px; font-weight: 400; text-align: center; width: 310px; margin-left: -20px; margin-bottom: 14px; }
  .services ul { list-style: none; font-size: 14px; line-height: 19.9px; }
  .services li { position: relative; padding-left: 16px; }
  .services li::before { content: ""; position: absolute; left: 0; top: 8px; width: 4px; height: 4px; border-radius: 50%; background: var(--purple); }
  .services ul ul { margin-left: 26px; }
  .services ul ul li { padding-left: 14px; }
  .services ul ul li::before { background: var(--orange); }

  .footer-band { position: absolute; left: 0; bottom: 0; width: 100%; height: 48px; background: var(--purple); border-top: 5px solid var(--orange); z-index: 1; }
  .footer-band__url { position: absolute; left: 358px; width: 358px; top: 8px; text-align: center; color: #fff; font-size: 16px; letter-spacing: .3px; }

  .testimonial { position: absolute; z-index: 2; background: var(--quote-grey); color: #fff; text-align: center; font-size: 12.5px; line-height: 15.9px; padding: 40px 20px 10px; }
  .testimonial__name { font-family: "Arvo", Georgia, serif; font-weight: 700; font-size: 12px; line-height: 16px; }
  .testimonial__badge { position: absolute; left: 50%; top: -28px; transform: translateX(-50%); width: 48px; height: 48px; border-radius: 50%; background: #fff; border: 1.5px solid var(--purple); display: flex; align-items: center; justify-content: center; font-family: "Arvo", Georgia, serif; font-weight: 700; font-size: 40px; color: var(--quote-grey); line-height: 1; padding-top: 16px; }
  .testimonial--owen { left: 29px; top: 659px; width: 282px; height: 155px; padding-top: 36px; }
  .testimonial--grant { left: 398px; top: 290px; width: 282px; height: 340px; }
  .testimonial--ruth { left: 758px; top: 593px; width: 282px; height: 222px; padding-top: 36px; }
</style>
</head>
<body>
<main class="brochure">
  <section class="panel panel--left"></section>
  <section class="panel panel--middle"></section>
  <section class="panel panel--right"></section>

  <div class="scene scene--middle-lake" role="img" aria-label="Photograph of a calm northern lake with rocks, reeds and evergreen shoreline"></div>
  <div class="scene scene--left-shore" role="img" aria-label="Photograph of a forested lakeshore"></div>
  <div class="scene scene--right-forest" role="img" aria-label="Photograph of spruce forest along a lake"></div>

  <svg class="scene scene--lake-top" viewBox="0 0 716 260" role="img" aria-label="Photograph of a wilderness lake under a blue sky with spruce trees">
    <defs>
      <linearGradient id="lakeTone" x1="0" y1="0" x2="0" y2="1">
        <stop offset="0" stop-color="#9dbfdf"/>
        <stop offset=".22" stop-color="#e3eaf0"/>
        <stop offset=".42" stop-color="#33502f"/>
        <stop offset=".62" stop-color="#3d5638"/>
        <stop offset=".8" stop-color="#5a6a70"/>
        <stop offset="1" stop-color="#2f3833"/>
      </linearGradient>
    </defs>
    <path d="M0 0 H716 V170 C690 230 610 252 470 250 C330 248 170 226 0 244 Z" fill="url(#lakeTone)"/>
    <path d="M0 244 C110 222 230 208 320 222 C220 216 110 228 0 258 Z" fill="var(--orange)"/>
    <path d="M716 170 C700 236 620 258 470 254 C610 248 690 226 716 205 Z" fill="var(--purple)"/>
  </svg>

  <h1 class="headline">Guiding Responsible Philanthropy <strong>Improving Board Governance</strong></h1>

  <article class="what-we-do">
    <h2 class="section-title">What we do:</h2>
    <h3 class="subhead">Organizational Clients</h3>
    <p class="body-copy">20th century developmental psychologist Anders Halvik asserted that for individuals, conflict and crisis are positive and necessary; they are "sources of growth, strength, and commitment." We believe the same can be true of organizations. MCA helps nonprofits manage change and emerge triumphantly. Through coaching, we help organizations implement practices to maximize efficiency and effectiveness - whether preparing for transition, coping with chaos, or simply pursuing continued high performance - by working directly with board members and staff.<br>Our methods are informed by research and honed by over 20 years of practice.</p>
    <h3 class="subhead">Private Clients</h3>
    <p class="body-copy">MCA philanthropic counsel helps individuals adopt impactful practices in their charitable endeavors.</p>
  </article>

  <div class="brand">
    <span class="brand__mark"></span>
    <span class="brand__name">Morrow Civic Advisors</span>
  </div>

  <section class="services">
    <h2 class="services__title">Services</h2>
    <ul>
      <li>Board and Senior Staff Coaching</li>
      <li>Workshops, Seminars and Retreats including:
        <ul>
          <li>Roles &amp; Responsibilities</li>
          <li>Fundraising</li>
          <li>Succession Planning</li>
          <li>Board Self-Assessments</li>
          <li>Strategic Planning</li>
          <li>Board Recruitment Training</li>
          <li>Communications Development</li>
          <li>Grassroots Advocacy</li>
          <li>Mergers &amp; Acquisitions</li>
        </ul>
      </li>
      <li>Philanthropic Counsel</li>
      <li>Board Placement</li>
      <li>Board Member Recruitment</li>
      <li>Board Retreat Planning &amp; Facilitation</li>
    </ul>
  </section>

  <div class="footer-band">
    <p class="footer-band__url">MorrowCivicAdvisors.com</p>
  </div>

  <blockquote class="testimonial testimonial--grant">
    <span class="testimonial__badge">“</span>
    <p class="testimonial__name">Grant Ellison, CTFA (Client, Philanthropist)</p>
    <p>“I’ve had the honor and distinct privilege of working with Dana through her Board Coaching &amp; Training program. The board self-assessment process is thorough, insightful and necessary, if like me, you are challenged with finding the right organization to align with. Leveraging her expertise, guidance and deep connections throughout the Non-Profit space, Dana carefully screened several organizations as potential candidates, and went so far as to arrange introductory meetings with a select few. The entire process was educational, and an exceptional experience.”</p>
  </blockquote>

  <blockquote class="testimonial testimonial--owen">
    <span class="testimonial__badge">“</span>
    <p class="testimonial__name">Owen Castell (Client, Journalist and Broadcaster)</p>
    <p>“Dana is at forefront of the new era of responsible philanthropy … Most importantly, she has the rare ability to take a vision and turn it into a coherent plan of action.”</p>
  </blockquote>

  <blockquote class="testimonial testimonial--ruth">
    <span class="testimonial__badge">“</span>
    <p class="testimonial__name">Ruth Alder (Past Chairman, Northern Guild for Arts Health)</p>
    <p>“I wish you could have heard the board’s comments. They were unanimously and warmly enthusiastic, saying it was the best thing we, as a board, have ever done... Thank you for the thought and combination of emotional and intellectual intelligence that you brought to the presentation.”</p>
  </blockquote>
</main>
</body>
</html>
```